Spring ORVu 2016 Training Weekend Program Booklet

We need graphic design for the program booklet for our Spring leadership development training weekend for minority MBA students working in Finance. The design should include the colors in the attached logo and be fun and young (but somewhat conservative). The final files should be either Adobe InDesign or Illustrator so we can lay in text and images as needed. The layout will be:
Front Cover
Interior Page Template with Design
Inside Front Cover - Table of Contents
Page 1. Welcome Letter
Pages 2-3. Sponsor Acknowledgement
Pages 4-5. Program Agenda
Page 6. Listing of speakers and presenters
Page 7. Upcoming Events (Calendar)
Pages 8-10 Student Directory
Page 11. Listing of School Captains
Page 12. Resource Documents (title page)
Pages 13-16 Resource Documents
Pages 17 - 24. Notes Pages (blank for taking notes)
A sample of last season's book is provided.
Target Market(s)
Minority business school students attending top business schools (i.e Penmoor, Dunstry, Calbrook, etc.)
Industry/Entity Type
Financial Service

```html
<!DOCTYPE html>
<html lang="en">
<head>
<meta charset="utf-8">
<title>ORVu Booklet – Calendar and Student Directory</title>
<link rel="stylesheet" href="https://fonts.googleapis.com/css2?family=Source+Sans+3:wght@400;600;700&display=swap">
<style>
:root{
  --sky:#84afd6;
  --mist:#cddde4;
  --sage:#cfd69a;
  --teal:#86b7c9;
  --olive:#b5c15a;
  --ocean:#0a87bf;
  --ink:#1a1a1a;
  --paper:#ffffff;
}
*{margin:0;padding:0;box-sizing:border-box}
html,body{width:1200px;height:776px;overflow:hidden;background:var(--paper)}
body{font-family:"Source Sans 3",Arial,sans-serif;color:var(--ink)}
.spread{position:relative;width:1224px;height:792px;transform:scale(0.9804);transform-origin:0 0;overflow:hidden}
.page{position:absolute;top:0;height:792px;width:612px}
.page--left{left:0}
.page--right{left:612px}
.swoosh{position:absolute;inset:0}
.page-title{position:absolute;top:63px;height:36px;color:var(--paper);font-weight:600;font-size:24px;letter-spacing:.3px;line-height:36px;padding-left:36px}
.page--left .page-title{left:0;width:450px;background:var(--sky)}
.page--right .page-title{left:0;width:450px;background:var(--sage)}
.month{position:absolute;left:72px}
.month-bar{height:16px;color:var(--paper);font-weight:700;font-size:13px;line-height:16px;padding-left:6px}
.event{display:flex;font-size:13px;line-height:12px}
.event:first-of-type{margin-top:11px}
.event-day{width:42px;padding-left:7px;font-weight:700}
.folio{position:absolute;left:36px;top:754px;font-size:8px;font-weight:700}
.directory{position:absolute;top:110px;font-size:9.5px;line-height:12px}
.directory--a{left:36px}
.directory--b{left:312px}
.group{height:108px}
.group-title{font-weight:700}
.brand{position:absolute;top:40px;left:506px;color:var(--ink);font-weight:400;font-size:13px;letter-spacing:.5px}
</style>
</head>
<body>
<div class="spread">

  <section class="page page--left">
    <h1 class="page-title">UPCOMING EVENTS - CALENDAR</h1>

    <div class="month" style="top:143px"><div class="month-bar" style="width:413px;background:var(--mist)">MARCH</div>
      <p class="event"><span class="event-day">12</span>Event • Location • Time • Cost</p><p class="event"><span class="event-day">19</span>Event • Location • Time • Cost</p></div>
    <div class="month" style="top:202px"><div class="month-bar" style="width:353px;background:var(--sage)">APRIL</div>
      <p class="event"><span class="event-day">12</span>Event • Location • Time • Cost</p><p class="event"><span class="event-day">19</span>Event • Location • Time • Cost</p></div>
    <div class="month" style="top:262px"><div class="month-bar" style="width:353px;background:var(--teal)">MAY</div>
      <p class="event"><span class="event-day">12</span>Event • Location • Time • Cost</p><p class="event"><span class="event-day">19</span>Event • Location • Time • Cost</p></div>
    <div class="month" style="top:321px"><div class="month-bar" style="width:374px;background:var(--olive)">JUNE</div>
      <p class="event"><span class="event-day">12</span>Event • Location • Time • Cost</p><p class="event"><span class="event-day">19</span>Event • Location • Time • Cost</p></div>
    <div class="month" style="top:380px"><div class="month-bar" style="width:353px;background:var(--sky)">JULY</div>
      <p class="event"><span class="event-day">12</span>Event • Location • Time • Cost</p><p class="event"><span class="event-day">19</span>Event • Location • Time • Cost</p></div>
    <div class="month" style="top:440px"><div class="month-bar" style="width:405px;background:var(--ocean)">AUGUST</div>
      <p class="event"><span class="event-day">12</span>Event • Location • Time • Cost</p><p class="event"><span class="event-day">19</span>Event • Location • Time • Cost</p></div>
    <div class="month" style="top:500px"><div class="month-bar" style="width:360px;background:var(--teal)">SEPTEMBER</div>
      <p class="event"><span class="event-day">12</span>Event • Location • Time • Cost</p><p class="event"><span class="event-day">19</span>Event • Location • Time • Cost</p></div>
    <div class="month" style="top:559px"><div class="month-bar" style="width:330px;background:var(--olive)">OCTOBER</div>
      <p class="event"><span class="event-day">12</span>Event • Location • Time • Cost</p><p class="event"><span class="event-day">19</span>Event • Location • Time • Cost</p></div>
    <div class="month" style="top:619px"><div class="month-bar" style="width:387px;background:var(--teal)">NOVEMBER</div>
      <p class="event"><span class="event-day">12</span>Event • Location • Time • Cost</p><p class="event"><span class="event-day">19</span>Event • Location • Time • Cost</p></div>
    <div class="month" style="top:678px"><div class="month-bar" style="width:432px;background:var(--sage)">DECEMBER</div>
      <p class="event"><span class="event-day">12</span>Event • Location • Time • Cost</p><p class="event"><span class="event-day">19</span>Event • Location • Time • Cost</p></div>

    <span class="folio">7</span>
  </section>

  <section class="page page--right">
    <svg class="swoosh" viewBox="0 0 612 792" width="612" height="792" aria-hidden="true">
      <path d="M0,0 H450 Q170,60 0,280 Z" fill="var(--ocean)"/>
      <path d="M0,648 Q180,760 330,752 Q480,740 612,640 V792 H0 Z" fill="var(--ocean)"/>
    </svg>

    <p class="brand">ORVu</p>

    <h2 class="page-title">STUDENT DIRECTORY</h2>

    <div class="directory directory--a">
      <div class="group"><p class="group-title">CATEGORY</p><p>Listing</p><p>Listing</p><p>Listing</p><p>Listing</p><p>Listing</p><p>Listing</p><p>Listing</p></div>
      <div class="group"><p class="group-title">CATEGORY</p><p>Listing</p><p>Listing</p><p>Listing</p><p>Listing</p><p>Listing</p><p>Listing</p><p>Listing</p></div>
      <div class="group"><p class="group-title">CATEGORY</p><p>Listing</p><p>Listing</p><p>Listing</p><p>Listing</p><p>Listing</p><p>Listing</p><p>Listing</p></div>
      <div class="group"><p class="group-title">CATEGORY</p><p>Listing</p><p>Listing</p><p>Listing</p><p>Listing</p><p>Listing</p><p>Listing</p><p>Listing</p></div>
      <div class="group"><p class="group-title">CATEGORY</p><p>Listing</p><p>Listing</p><p>Listing</p><p>Listing</p><p>Listing</p><p>Listing</p><p>Listing</p></div>
      <div class="group"><p class="group-title">CATEGORY</p><p>Listing</p><p>Listing</p><p>Listing</p><p>Listing</p><p>Listing</p><p>Listing</p><p>Listing</p></div>
    </div>

    <div class="directory directory--b">
      <div class="group"><p class="group-title">CATEGORY</p><p>Listing</p><p>Listing</p><p>Listing</p><p>Listing</p><p>Listing</p><p>Listing</p><p>Listing</p></div>
      <div class="group"><p class="group-title">CATEGORY</p><p>Listing</p><p>Listing</p><p>Listing</p><p>Listing</p><p>Listing</p><p>Listing</p><p>Listing</p></div>
      <div class="group"><p class="group-title">CATEGORY</p><p>Listing</p><p>Listing</p><p>Listing</p><p>Listing</p><p>Listing</p><p>Listing</p><p>Listing</p></div>
      <div class="group"><p class="group-title">CATEGORY</p><p>Listing</p><p>Listing</p><p>Listing</p><p>Listing</p><p>Listing</p><p>Listing</p><p>Listing</p></div>
      <div class="group"><p class="group-title">CATEGORY</p><p>Listing</p><p>Listing</p><p>Listing</p><p>Listing</p><p>Listing</p><p>Listing</p><p>Listing</p></div>
      <div class="group"><p class="group-title">CATEGORY</p><p>Listing</p><p>Listing</p><p>Listing</p><p>Listing</p><p>Listing</p><p>Listing</p><p>Listing</p></div>
    </div>
  </section>

</div>
</body>
</html>
```